CuraNex System Web Page Design

This project is to design 6 pages of a web based medical system for clinics, hospitals, drugs suppliers, general items suppliers, insurance company, laboratories and patients (basically all parties which could be involved in).We want the designs of the browser, button, icon and layout are based on Vex, which is user friendly, looks professional, simple and neat but with powerful functions. We have uploaded few pictures of another system, please do not copy its design because this is not what we are looking for, the pictures are for you to know the elements should be included in our pages. CuraNex web-base system, design 6 pages1. Login PageShould include the following elements-company id with input field-login id with input field-password with input field2. Main Page (Navigation page)Should include the following elements-Appointment-Consultation-Patient-Drugs inventory -General supplies inventory -Laboratory-Suppliers-Insurance-Reports 3. Appointment PageShould include all the the elements in the respective pictures plus the followings-Daily View, Weekly View, Monthly View buttons4. Consultation PageShould include all the the elements in the respective picture5. Patient Page5.1 General information Should include all the the elements in the respective picture5.2 medical history/lab reportsShould include all the the elements in the respective picture plus the followings-Notify patient button-Share report button.
Updated on 28 Nov:
Please stop using Ward Keystone in your designs which is not the name of our system. We have just rename our system to CuraNex, please take note.
We need the system to look professional not playful, do not use too many colors and playful icons.
professional users

```html
<!DOCTYPE html>
<html lang="en">
<head>
<meta charset="utf-8">
<title>CuraNex – Main Navigation</title>
<link href="https://fonts.googleapis.com/css2?family=Roboto:wght@300;400;500;700&display=swap" rel="stylesheet">
<style>
  :root {
    --brand-blue: #0a6fbd;
    --text-grey: #4a4a4a;
    --panel-bg: #f1f1f1;
    --panel-border: #d2d2d2;
    --tile-bg: #ffffff;
    --tile-border: #cfcfcf;
    --page-bg: #ffffff;
    --field-border: #bdbdbd;
    --field-text: #a8a8a8;
  }
  * { margin: 0; padding: 0; box-sizing: border-box; }
  html, body { width: 1200px; height: 700px; overflow: hidden; background: var(--page-bg); }
  body { font-family: "Roboto", Arial, sans-serif; position: relative; }

  .brand {
    position: absolute; left: 66px; top: 50px;
    font-size: 25px; font-weight: 700; color: var(--brand-blue);
    letter-spacing: -0.3px;
  }
  .top-nav {
    position: absolute; top: 57px; right: 52px;
    display: flex; align-items: center; gap: 34px;
    font-size: 17px; font-weight: 300; color: var(--text-grey);
  }
  .top-nav .support { display: flex; align-items: center; gap: 12px; }
  .top-nav .support svg { width: 17px; height: 17px; }
  .search-field {
    width: 131px; height: 24px; border: 1px solid var(--field-border); border-radius: 12px;
    display: flex; align-items: center; justify-content: space-between;
    padding: 0 8px 0 11px; font-size: 11px; color: var(--field-text); margin-left: 6px;
  }
  .search-field svg { width: 11px; height: 11px; }

  .nav-panel {
    position: absolute; left: 53px; top: 122px; width: 1094px; height: 530px;
    background: var(--panel-bg); border: 1px solid var(--panel-border); border-radius: 30px;
  }
  .module-row {
    position: absolute; left: 0; width: 100%;
    display: flex; justify-content: center; gap: 0;
  }
  .row-1 { top: 54px; }
  .row-2 { top: 280px; }
  .module { width: 200px; text-align: center; }
  .module-tile {
    width: 145px; height: 145px; margin: 0 auto;
    background: var(--tile-bg); border: 1px solid var(--tile-border); border-radius: 34px;
    display: flex; align-items: center; justify-content: center;
  }
  .module-tile svg { width: 84px; height: 84px; }
  .module-label {
    margin-top: 20px; font-size: 18px; font-weight: 500; color: var(--brand-blue);
    letter-spacing: 0.2px; white-space: nowrap;
  }
</style>
</head>
<body>
  <div class="brand">CuraNex</div>

  <nav class="top-nav">
    <span class="support">
      <svg viewBox="0 0 20 20" aria-hidden="true"><g fill="#111"><circle cx="10" cy="10" r="6"/><rect x="8.2" y="1" width="3.6" height="18"/><rect x="8.2" y="1" width="3.6" height="18" transform="rotate(45 10 10)"/><rect x="8.2" y="1" width="3.6" height="18" transform="rotate(90 10 10)"/><rect x="8.2" y="1" width="3.6" height="18" transform="rotate(135 10 10)"/></g><circle cx="10" cy="10" r="2.4" fill="#fff"/></svg>
      Support
    </span>
    <span>Language</span>
    <span>Sign out</span>
    <div class="search-field"><span>Search</span>
      <svg viewBox="0 0 12 12" aria-hidden="true"><circle cx="7" cy="5" r="3.5" fill="none" stroke="#999" stroke-width="1.4"/><line x1="4.5" y1="7.5" x2="1" y2="11" stroke="#999" stroke-width="1.6"/></svg>
    </div>
  </nav>

  <main class="nav-panel">
    <div class="module-row row-1">
      <div class="module">
        <div class="module-tile">
          <svg viewBox="0 0 100 100" aria-hidden="true" fill="var(--brand-blue)">
            <path d="M6 18h74v40h-8V32H14v50h42v8H6z"/>
            <rect x="18" y="8" width="7" height="18" rx="3"/><rect x="61" y="8" width="7" height="18" rx="3"/>
            <circle cx="72" cy="72" r="22"/><circle cx="72" cy="72" r="16" fill="#fff"/>
            <path d="M69 60h6v11h9v6H69z"/>
          </svg>
        </div>
        <div class="module-label">APPOINTMENT</div>
      </div>

      <div class="module">
        <div class="module-tile">
          <svg viewBox="0 0 100 100" aria-hidden="true" fill="var(--brand-blue)">
            <path d="M10 14h80v56H42L22 88V70H10z"/>
            <rect x="45" y="25" width="10" height="34" fill="#fff"/>
            <rect x="33" y="37" width="34" height="10" fill="#fff"/>
          </svg>
        </div>
        <div class="module-label">CONSULTATION</div>
      </div>

      <div class="module">
        <div class="module-tile">
          <svg viewBox="0 0 100 100" aria-hidden="true">
            <path d="M50 8c14 0 22 10 22 24 0 10-4 18-10 22 16 4 26 10 28 16v18H10V70c2-6 12-12 28-16-6-4-10-12-10-22 0-14 8-24 22-24z" fill="none" stroke="var(--brand-blue)" stroke-width="6" stroke-linejoin="round"/>
          </svg>
        </div>
        <div class="module-label">PATIENT</div>
      </div>

      <div class="module">
        <div class="module-tile">
          <svg viewBox="0 0 100 100" aria-hidden="true" fill="var(--brand-blue)">
            <rect x="34" y="6" width="32" height="12" rx="2"/>
            <rect x="24" y="22" width="52" height="72" rx="6"/>
            <rect x="44" y="40" width="12" height="36" fill="#fff"/>
            <rect x="32" y="52" width="36" height="12" fill="#fff"/>
          </svg>
        </div>
        <div class="module-label">DRUGS INVENTORY</div>
      </div>

      <div class="module">
        <div class="module-tile">
          <svg viewBox="0 0 100 100" aria-hidden="true" fill="none" stroke="var(--brand-blue)" stroke-width="7" stroke-linejoin="round">
            <path d="M50 8l38 18v48L50 92 12 74V26z"/>
            <path d="M12 26l38 18 38-18M50 44v48"/>
          </svg>
        </div>
        <div class="module-label">GENERAL SUPPLIES</div>
      </div>
    </div>

    <div class="module-row row-2">
      <div class="module">
        <div class="module-tile">
          <svg viewBox="0 0 100 100" aria-hidden="true" fill="var(--brand-blue)">
            <path d="M34 6h32v8h-5v26l24 42c3 6 0 12-6 12H21c-6 0-9-6-6-12l24-42V14h-5z"/>
            <path d="M30 64h40l10 18H20z" fill="#fff"/>
          </svg>
        </div>
        <div class="module-label">LABORATORY</div>
      </div>

      <div class="module">
        <div class="module-tile">
          <svg viewBox="0 0 100 100" aria-hidden="true" fill="var(--brand-blue)">
            <rect x="4" y="22" width="56" height="48" rx="3"/>
            <path d="M64 36h18l14 18v16H64z"/>
            <path d="M70 42h10l9 12H70z" fill="#fff"/>
            <circle cx="24" cy="76" r="10" stroke="#fff" stroke-width="4"/>
            <circle cx="78" cy="76" r="10" stroke="#fff" stroke-width="4"/>
          </svg>
        </div>
        <div class="module-label">SUPPLIERS</div>
      </div>

      <div class="module">
        <div class="module-tile">
          <svg viewBox="0 0 100 100" aria-hidden="true">
            <path d="M50 6l36 12v28c0 24-16 40-36 48C30 86 14 70 14 46V18z" fill="var(--brand-blue)"/>
            <path d="M34 50l12 12 22-24" fill="none" stroke="#fff" stroke-width="8" stroke-linecap="round" stroke-linejoin="round"/>
          </svg>
        </div>
        <div class="module-label">INSURANCE</div>
      </div>

      <div class="module">
        <div class="module-tile">
          <svg viewBox="0 0 100 100" aria-hidden="true" fill="var(--brand-blue)">
            <path d="M20 6h40l22 22v66H20z"/>
            <path d="M28 14h28v20h18v52H28z" fill="#fff"/>
            <rect x="36" y="44" width="20" height="5"/><rect x="36" y="55" width="30" height="5"/><rect x="36" y="66" width="30" height="5"/>
          </svg>
        </div>
        <div class="module-label">REPORTS</div>
      </div>
    </div>
  </main>
</body>
</html>
```